Modern Medical Optometry Website

We need mordern, Patient friendly website. Easy to navigate and enhance our advance medical technology and excellent patient care.
1. HOME PAGE
2. OUR TEAM PAGE
3. EYECARE PAGE - VISION SERVICES, EYE EXAMS, KERATOCONUS CENTER, GLAUCOMA , DIABITES, TORVANEX EXAM, DIGITAL RETINAL, OCT.
4. MYOPIA CONTROL CLINIC
5. DRY EYE CLINIC
6. EYEWEAR
7. PATIENT CENTER - BLOG
7. CONTACT US
This is our current website www.brindlecove.com
and We want to add more content and a cleaner design like these website
http://tamsworthoptometry.com/
https://www.klmhaven.com/

```html
<!DOCTYPE html>
<html lang="en">
<head>
<meta charset="utf-8">
<title>Brindle Cove Optometry</title>
<link href="https://fonts.googleapis.com/css2?family=Raleway:wght@400;500;600;700;800&display=swap" rel="stylesheet">
<style>
:root{
  --teal:#1b93b0;
  --teal-dark:#137d98;
  --teal-soft:#4fb3cb;
  --yellow:#f6d93b;
  --yellow-soft:#f8e36e;
  --ink:#333a40;
  --muted:#7a8288;
  --light:#f3f4f5;
  --white:#ffffff;
  --dark:#2b2f33;
}
*{box-sizing:border-box;margin:0;padding:0}
html,body{width:1200px;height:4348px;overflow:hidden}
body{font-family:"Raleway",sans-serif;color:var(--ink);background:var(--white);position:relative}
section,header,footer{position:absolute;left:0;width:1200px}
svg{display:block}

/* header */
.site-header{top:0;height:190px;background:var(--white)}
.topbar{position:absolute;right:0;top:0;width:760px;height:44px;background:var(--teal);display:flex;align-items:center;padding-left:40px;gap:30px;color:var(--white);font-size:15px;font-weight:600}
.topbar .item{display:flex;align-items:center;gap:10px}
.topbar .socials{display:flex;gap:0;margin-left:auto;margin-right:40px}
.topbar .socials span{width:44px;height:44px;border-left:1px solid rgba(255,255,255,.3);display:flex;align-items:center;justify-content:center}
.topbar .socials span i{width:12px;height:12px;border-radius:50%;background:var(--white);display:block}
.brand{position:absolute;left:78px;top:10px;width:112px;height:170px;background:var(--white);box-shadow:0 2px 12px rgba(0,0,0,.12);display:flex;flex-direction:column;align-items:center;justify-content:center;gap:10px}
.brand .mark{width:58px;height:58px;background:var(--yellow)}
.brand .name{font-size:14px;font-weight:700;color:var(--ink);text-align:center;line-height:1.15}
.main-nav{position:absolute;left:220px;top:108px;display:flex;gap:40px;font-size:16px;font-weight:600;color:var(--muted);text-transform:uppercase;letter-spacing:.3px}
.main-nav .active{color:var(--teal)}
.main-nav .search{margin-left:-10px}

/* hero */
.hero{top:190px;height:580px;background:linear-gradient(110deg,#1e9cba 0%,#2aa7c3 55%,#58bdd3 100%)}
.hero h1{position:absolute;left:78px;top:125px;font-size:56px;line-height:1.15;font-weight:500;color:var(--white);letter-spacing:2px}
.hero p{position:absolute;left:78px;top:276px;width:440px;font-size:16px;line-height:1.65;color:var(--white)}
.btn{display:inline-flex;align-items:center;justify-content:center;background:var(--yellow);color:var(--ink);font-weight:700;text-transform:uppercase;font-size:16px}
.hero .btn{position:absolute;left:78px;top:375px;width:238px;height:56px}
.hero-ring{position:absolute;left:565px;top:12px;width:500px;height:500px;border-radius:50%;background:var(--yellow);padding:22px}
.hero-ring .photo{width:100%;height:100%;border-radius:50%;background:radial-gradient(circle at 45% 40%,#f4d6c2,#d9a98a 55%,#8fc7d6 100%);border:10px solid var(--white)}
.dots{position:absolute;left:560px;top:488px;display:flex;gap:12px}
.dots span{width:16px;height:16px;border-radius:50%;border:2px solid var(--white)}
.dots .on{background:var(--white)}

/* promise */
.promise{top:770px;height:345px;background:var(--white)}
.promise .kicker{position:absolute;left:78px;top:50px;font-size:16px;color:var(--muted);text-transform:uppercase;letter-spacing:.5px}
.promise h2{position:absolute;left:78px;top:88px;width:460px;font-size:38px;line-height:1.2;font-weight:500;text-transform:uppercase;color:var(--ink)}
.promise h2 strong{color:var(--teal);font-weight:700}
.promise .copy{position:absolute;left:560px;top:50px;width:560px;font-size:15px;line-height:1.75;color:var(--muted)}
.promise .copy p+p{margin-top:20px}

/* feature cards */
.features{top:1115px;height:420px}
.card{position:absolute;color:var(--white);padding:38px 30px}
.card.teal{background:var(--teal);top:35px;height:336px;width:342px}
.card.yellow{background:var(--yellow);color:var(--ink);top:0;height:406px;width:360px;left:420px;box-shadow:0 10px 24px rgba(0,0,0,.15)}
.card.left{left:78px}
.card.right{left:780px}
.card h3{font-size:26px;font-weight:500;margin:22px 0 18px}
.card p{font-size:14px;line-height:1.7}
.card .phone{font-size:28px;font-weight:700;margin-top:28px}
.hours li{list-style:none;font-size:15px;line-height:1.3;padding:8px 0;border-bottom:1px solid rgba(255,255,255,.35)}
.hours li:last-child{border-bottom:0}

/* about */
.about{top:1595px;height:470px}
.about-band{position:absolute;left:0;top:80px;width:1200px;height:390px;background:var(--light)}
.about .photo{position:absolute;left:78px;top:0;width:522px;height:470px;border-radius:16px;box-shadow:0 6px 20px rgba(0,0,0,.2);background:linear-gradient(100deg,#f7f8fa 0%,#e9eef2 45%,#9dc4dd 70%,#4a7fae 100%)}
.about-text{position:absolute;left:660px;top:135px;width:500px;display:flex;flex-direction:column;align-items:flex-start}
.about .kicker{font-size:16px;color:var(--muted);text-transform:uppercase}
.about h2{margin-top:6px;font-size:32px;line-height:1.2;font-weight:700;color:var(--teal);text-transform:uppercase;white-space:nowrap}
.about p{margin-top:18px;width:470px;font-size:15px;line-height:1.8;color:var(--muted)}
.about .btn{margin-top:22px;width:122px;height:50px}

/* services */
.services{top:2130px;height:930px;background:linear-gradient(180deg,#1f98b5,#2aa4c1)}
.services .kicker{position:absolute;left:0;width:1200px;top:55px;text-align:center;font-size:16px;color:rgba(255,255,255,.85);text-transform:uppercase;letter-spacing:1px}
.services h2{position:absolute;left:0;width:1200px;top:82px;text-align:center;font-size:40px;font-weight:700;color:var(--white);text-transform:uppercase}
.tile{position:absolute;width:324px;height:314px;border:5px solid var(--white);box-shadow:0 8px 18px rgba(0,0,0,.2)}
.tile.featured{border:10px solid rgba(255,255,255,.55);background:var(--yellow)!important;display:flex;align-items:center;justify-content:center}
.tile.featured span{font-size:30px;font-weight:600;text-transform:uppercase;color:var(--ink)}

/* testimonials */
.feedback{top:3060px;height:520px;background:var(--light)}
.feedback .kicker{position:absolute;left:0;width:1200px;top:78px;text-align:center;font-size:16px;color:var(--muted);text-transform:uppercase}
.feedback h2{position:absolute;left:0;width:1200px;top:104px;text-align:center;font-size:40px;font-weight:700;color:var(--teal);text-transform:uppercase}
.review{position:absolute;top:190px;width:336px;height:196px;background:var(--white);box-shadow:0 4px 14px rgba(0,0,0,.1)}
.review .quote{position:absolute;left:0;top:36px;width:50px;height:94px;background:var(--yellow);display:flex;align-items:center;justify-content:center;font-size:48px;font-weight:800;color:var(--ink)}
.review p{position:absolute;left:70px;top:24px;right:22px;font-size:14px;line-height:1.7;color:var(--muted)}
.reviewer{position:absolute;top:405px;width:336px;display:flex;align-items:center;gap:14px}
.reviewer .avatar{width:60px;height:60px;border:3px solid var(--yellow);background:linear-gradient(135deg,#cfe3ea,#8fb7c6)}
.reviewer .who{font-size:15px;color:var(--teal);font-weight:600;line-height:1.2}
.reviewer .stars{color:#f2b82b;font-size:16px;letter-spacing:1px}
.reviewer .source{margin-left:auto;font-size:26px;font-weight:700;color:var(--ink)}

/* brands */
.brands{top:3580px;height:290px;background:var(--white)}
.brand-item{position:absolute;top:60px;width:170px;text-align:center}
.brand-item .label{font-size:20px;font-weight:700;color:#111;text-transform:uppercase;letter-spacing:.5px;white-space:nowrap;height:28px}
.brand-item .frame{margin:50px auto 0;width:130px;height:56px;border-radius:28px;background:linear-gradient(90deg,#d8d2cb,#8b8178 50%,#d8d2cb)}

/* footer */
.site-footer{top:3870px;height:478px;background:var(--yellow)}
.col{position:absolute;top:58px;width:330px}
.col h4{font-size:20px;font-weight:700;color:var(--teal);margin-bottom:22px}
.col .line{display:flex;align-items:flex-start;gap:16px;font-size:15px;color:var(--ink);margin-bottom:18px;line-height:1.45}
.col .line svg{flex:none;margin-top:2px}
.map-btn{display:flex;align-items:center;justify-content:space-between;width:280px;height:42px;padding:0 20px;border-radius:21px;background:var(--dark);color:var(--white);font-size:14px;font-weight:500;margin-top:22px}
.hours-list{font-size:15px;line-height:1.75;color:var(--ink)}
.socials-round{display:flex;gap:12px;margin-top:20px}
.socials-round span{width:40px;height:40px;border-radius:50%;background:var(--teal)}
.socials-round span:last-child{background:var(--dark)}
.copyright{position:absolute;left:0;bottom:0;width:1200px;height:58px;border-top:1px solid rgba(0,0,0,.12);display:flex;align-items:center;justify-content:center;font-size:14px;color:var(--ink)}
.copyright b{color:var(--teal);margin:0 4px}
</style>
</head>
<body>

<header class="site-header">
  <div class="topbar">
    <span class="item">
      <svg width="16" height="16" viewBox="0 0 24 24" fill="#fff"><path d="M6.6 10.8a15.1 15.1 0 0 0 6.6 6.6l2.2-2.2c.3-.3.7-.4 1-.2 1.1.4 2.3.6 3.6.6.6 0 1 .4 1 1V20c0 .6-.4 1-1 1A17 17 0 0 1 3 4c0-.6.4-1 1-1h3.5c.6 0 1 .4 1 1 0 1.3.2 2.5.6 3.6.1.3 0 .7-.2 1z"/></svg>
      555-214-3080
    </span>
    <span class="item">
      <svg width="18" height="14" viewBox="0 0 24 18" fill="none" stroke="#fff" stroke-width="2"><rect x="1" y="1" width="22" height="16"/><path d="M1 1l11 9 11-9"/></svg>
      info@brindlecove.com
    </span>
    <div class="socials"><span><i></i></span><span><i></i></span><span><i></i></span><span><i></i></span></div>
  </div>
  <div class="brand">
    <div class="mark"></div>
    <div class="name">BRINDLE COVE<br>OPTOMETRY</div>
  </div>
  <nav class="main-nav">
    <span class="active">Home</span><span>Our Team</span><span>Eye Care</span><span>Myopia Control Clinic</span><span>Eyewear</span><span>Blog</span><span>Contact Us</span>
    <span class="search"><svg width="20" height="20" viewBox="0 0 24 24" fill="none" stroke="#1b93b0" stroke-width="2.5"><circle cx="10" cy="10" r="7"/><path d="M15 15l7 7"/></svg></span>
  </nav>
</header>

<section class="hero">
  <h1>BRINDLE COVE<br>OPTOMETRY</h1>
  <p>Complete eye care for every age, from first exams to advanced treatment, delivered with patience, precision and a friendly smile by our local team.</p>
  <span class="btn">Make an Appointment</span>
  <div class="hero-ring"><div class="photo" role="img" aria-label="Photo of a smiling mother and daughter during an eye exam"></div></div>
  <div class="dots"><span></span><span class="on"></span><span></span></div>
</section>

<section class="promise">
  <div class="kicker">The Brindle Cove Promise</div>
  <h2>Not just better care, <strong>but a better care experience</strong></h2>
  <div class="copy">
    <p>Welcome to Brindle Cove Optometry, where your vision and eye health are our sole priority. We take great pride in providing you with state-of-the-art eyecare matched with personal attention from our staff and doctors. Your quality of life is our goal and we believe that healthy eyesight is vital to achieving it.</p>
    <p>Our professional and personable staff is highly trained in helping you achieve and maintain healthy eyesight. Our optometrists have combined experiences and specialize in Orthokeratology (OrthoK), Ocular disease, Glaucoma diagnosis &amp; management.</p>
  </div>
</section>

<section class="features">
  <div class="card teal left">
    <svg width="70" height="40" viewBox="0 0 70 40" fill="none" stroke="#fff" stroke-width="3"><path d="M3 20C15 4 55 4 67 20 55 36 15 36 3 20z"/><circle cx="35" cy="20" r="9"/></svg>
    <h3>Emergency Cases</h3>
    <p>Caring for your eyes is important, call us any time you need urgent help with your vision.</p>
    <div class="phone">555-214-3080</div>
  </div>
  <div class="card yellow">
    <svg width="70" height="56" viewBox="0 0 70 56" fill="none" stroke="#333a40" stroke-width="3"><rect x="4" y="8" width="62" height="44" rx="4"/><path d="M4 20h62M18 2v12M52 2v12"/><circle cx="35" cy="36" r="8"/></svg>
    <h3>Doctor Timetable</h3>
    <p>Professional and certified doctors available throughout the week for exams, fittings and follow up visits.</p>
  </div>
  <div class="card teal right">
    <svg width="80" height="36" viewBox="0 0 80 36" fill="none" stroke="#fff" stroke-width="3"><circle cx="18" cy="20" r="13"/><circle cx="62" cy="20" r="13"/><path d="M31 18c3-4 15-4 18 0M5 16L2 6M75 16l3-10"/></svg>
    <h3>Opening Hours</h3>
    <ul class="hours">
      <li>Monday - Thursday: 9 am - 6 pm</li>
      <li>Friday: 8.30 am - 5 pm</li>
      <li>Closed on Sundays</li>
      <li>Please keep in mind we are closed for lunch 1-2 pm</li>
    </ul>
  </div>
</section>

<section class="about">
  <div class="about-band"></div>
  <div class="photo" role="img" aria-label="Photo of a young boy covering one eye beside an eye chart"></div>
  <div class="about-text">
    <div class="kicker">About</div>
    <h2>Brindle Cove Optometry</h2>
    <p>Our family practice has served the neighborhood for years, pairing modern diagnostic equipment with unhurried visits. We explain every result in plain words, help you choose the right lenses and frames, and build a care plan that fits your life. From routine checkups to specialty treatment, we are with you at every step.</p>
    <span class="btn">Bookwell</span>
  </div>
</section>

<section class="services">
  <div class="kicker">What we offer</div>
  <h2>Brindle Cove Services</h2>
  <div class="tile" style="left:78px;top:175px;background:linear-gradient(160deg,#e9eef1,#6e9fc4)" role="img" aria-label="Photo of the optometry team in scrubs"></div>
  <div class="tile featured" style="left:440px;top:175px"><span>Dry Eyes</span></div>
  <div class="tile" style="left:800px;top:175px;background:linear-gradient(160deg,#f2f2f2,#b9bcbe)" role="img" aria-label="Photo of eyeglasses resting on an eye chart"></div>
  <div class="tile" style="left:78px;top:538px;background:linear-gradient(160deg,#d9e6ee,#8eb2c8)" role="img" aria-label="Photo of a patient at an eye exam instrument"></div>
  <div class="tile" style="left:440px;top:538px;background:linear-gradient(160deg,#e8c9b5,#c08f74)" role="img" aria-label="Photo of a contact lens on a fingertip near an eye"></div>
  <div class="tile" style="left:800px;top:538px;background:linear-gradient(160deg,#f1f1f1,#a9b6c4)" role="img" aria-label="Photo of a doctor examining a child with a parent"></div>
</section>

<section class="feedback">
  <div class="kicker">Testimonial</div>
  <h2>Clients Feedback</h2>
  <div class="review" style="left:78px"><div class="quote">“</div><p>The staff were kind and patient, the exam was thorough and the doctor explained every result clearly. I left with glasses I love.</p></div>
  <div class="review" style="left:435px"><div class="quote">“</div><p>Booking was easy, the wait was short and my daughter felt relaxed the whole time. A caring team we will keep visiting.</p></div>
  <div class="review" style="left:790px"><div class="quote">“</div><p>Modern equipment, honest advice and a warm welcome. They found an issue early and followed up with real care and attention.</p></div>
  <div class="reviewer" style="left:98px"><div class="avatar" role="img" aria-label="Reviewer portrait"></div><div><div class="who">Daniel<br>Orvey</div><div class="stars">★★★★★</div></div><div class="source">Reviewly</div></div>
  <div class="reviewer" style="left:455px"><div class="avatar" role="img" aria-label="Reviewer portrait"></div><div><div class="who">Daniel<br>Orvey</div><div class="stars">★★★★★</div></div><div class="source">Localpin</div></div>
  <div class="reviewer" style="left:810px"><div class="avatar" role="img" aria-label="Reviewer portrait"></div><div><div class="who">Daniel<br>Orvey</div><div class="stars">★★★★★</div></div><div class="source">Bookwell</div></div>
</section>

<section class="brands">
  <div class="brand-item" style="left:70px"><div class="label">Verano</div><div class="frame" role="img" aria-label="Photo of dark sunglasses"></div></div>
  <div class="brand-item" style="left:250px"><div class="label">Halden</div><div class="frame" role="img" aria-label="Photo of tortoiseshell eyeglasses"></div></div>
  <div class="brand-item" style="left:430px"><div class="label">Marlowe &amp; Co.</div><div class="frame" role="img" aria-label="Photo of round brown sunglasses"></div></div>
  <div class="brand-item" style="left:610px"><div class="label">Strada</div><div class="frame" role="img" aria-label="Photo of light rimless eyeglasses"></div></div>
  <div class="brand-item" style="left:790px"><div class="label">Solenne</div><div class="frame" role="img" aria-label="Photo of black eyeglasses"></div></div>
  <div class="brand-item" style="left:970px"><div class="label">Kestrel</div><div class="frame" role="img" aria-label="Photo of gradient sunglasses"></div></div>
</section>

<footer class="site-footer">
  <div class="col" style="left:78px">
    <h4>Brindle Cove Optometry</h4>
    <div class="line"><svg width="18" height="18" viewBox="0 0 24 24" fill="#1b93b0"><path d="M6.6 10.8a15.1 15.1 0 0 0 6.6 6.6l2.2-2.2c.3-.3.7-.4 1-.2 1.1.4 2.3.6 3.6.6.6 0 1 .4 1 1V20c0 .6-.4 1-1 1A17 17 0 0 1 3 4c0-.6.4-1 1-1h3.5c.6 0 1 .4 1 1 0 1.3.2 2.5.6 3.6.1.3 0 .7-.2 1z"/></svg>555-214-3080</div>
    <div class="line"><svg width="18" height="18" viewBox="0 0 24 24" fill="#1b93b0"><path d="M6.6 10.8a15.1 15.1 0 0 0 6.6 6.6l2.2-2.2c.3-.3.7-.4 1-.2 1.1.4 2.3.6 3.6.6.6 0 1 .4 1 1V20c0 .6-.4 1-1 1A17 17 0 0 1 3 4c0-.6.4-1 1-1h3.5c.6 0 1 .4 1 1 0 1.3.2 2.5.6 3.6.1.3 0 .7-.2 1z"/></svg>555-214-3090</div>
    <div class="line"><svg width="18" height="14" viewBox="0 0 24 18" fill="none" stroke="#1b93b0" stroke-width="2"><rect x="1" y="1" width="22" height="16"/><path d="M1 1l11 9 11-9"/></svg>hello@brindlecove.com</div>
    <div class="line"><svg width="18" height="22" viewBox="0 0 24 30" fill="#1b93b0"><path d="M12 0a11 11 0 0 0-11 11c0 8 11 19 11 19s11-11 11-19A11 11 0 0 0 12 0zm0 15a4 4 0 1 1 0-8 4 4 0 0 1 0 8z"/></svg>4820 Larkspur Ave., Fernwood,<br>CA 90412</div>
    <div class="map-btn">Get directions on the map <svg width="40" height="10" viewBox="0 0 40 10" fill="none" stroke="#fff" stroke-width="1.5"><path d="M0 5h38M33 1l5 4-5 4"/></svg></div>
  </div>
  <div class="col" style="left:435px">
    <h4>Harbor Point</h4>
    <div class="line"><svg width="18" height="18" viewBox="0 0 24 24" fill="#1b93b0"><path d="M6.6 10.8a15.1 15.1 0 0 0 6.6 6.6l2.2-2.2c.3-.3.7-.4 1-.2 1.1.4 2.3.6 3.6.6.6 0 1 .4 1 1V20c0 .6-.4 1-1 1A17 17 0 0 1 3 4c0-.6.4-1 1-1h3.5c.6 0 1 .4 1 1 0 1.3.2 2.5.6 3.6.1.3 0 .7-.2 1z"/></svg>555-362-7140</div>
    <div class="line"><svg width="18" height="14" viewBox="0 0 24 18" fill="none" stroke="#1b93b0" stroke-width="2"><rect x="1" y="1" width="22" height="16"/><path d="M1 1l11 9 11-9"/></svg>harborpoint@brindlecove.com</div>
    <div class="line"><svg width="18" height="22" viewBox="0 0 24 30" fill="#1b93b0"><path d="M12 0a11 11 0 0 0-11 11c0 8 11 19 11 19s11-11 11-19A11 11 0 0 0 12 0zm0 15a4 4 0 1 1 0-8 4 4 0 0 1 0 8z"/></svg>2291 Quillan Rd., Suite 4,<br>Harbor Point, CA 90418</div>
    <div class="map-btn" style="margin-top:70px">Get directions on the map <svg width="40" height="10" viewBox="0 0 40 10" fill="none" stroke="#fff" stroke-width="1.5"><path d="M0 5h38M33 1l5 4-5 4"/></svg></div>
  </div>
  <div class="col" style="left:790px">
    <h4>Opening Hours</h4>
    <div class="hours-list">
      Monday - Thursday : <b>9 am - 6 pm</b><br>
      Friday : <b>8.30 am - 5 pm</b><br>
      Saturday : <b>8.30 am - 5 pm</b><br>
      Closed on <b>Sundays</b><br>
      Please keep in mind we are closed<br>for <b>lunch 1-2 pm</b>
    </div>
    <div class="socials-round"><span></span><span></span><span></span><span></span></div>
  </div>
  <div class="copyright">Copyright © <b>BRINDLE COVE OPTOMETRY</b> - 2018 . All Right Reserved</div>
</footer>

</body>
</html>
```